Business Card and Letterhead Design for Public Accounting Firm

Business card and letterhead design for a CPA Firm located in Orange County, CA. We're looking for a modern and professional design utilizing our existing logo. We'd like a clean "less is more" look, but also something that catches the eye. We provide a high level of service to our clients. Open to single or double sided business cards.

Additional info: color numbers on logo
Blue :
R 0
G 83
B 125

#00537D

Silver :

R 154
G 154
B 154

#9A9A9A

Target Market(s)

Businesses and individuals

Industry/Entity Type

Accounting

Contact Information for Business Card

Moss Whitfield & Danby LLP - 4827 Larkspur Vale Road, Irvine, CA 92614 - (949)731-2864 - mwdaccts.example

Font styles to use
Serif
Sans Serif
Other font styles liked:
• See font file uploaded

Colors
0054AA
0677BA
7BADD7
CADEEF
E8F1F8

Requirements
Nice to have
• Possibly use the font file provided which matches our logo, but adjust to be not in all caps

```html
<!DOCTYPE html>
<html lang="en">
<head>
<meta charset="utf-8">
<title>Moss Whitfield &amp; Danby LLP – Business Card</title>
<link href="https://fonts.googleapis.com/css2?family=Playfair+Display:wght@400&display=swap" rel="stylesheet">
<style>
  :root {
    --backdrop: #e6e2dc;
    --card-white: #ffffff;
    --brand-blue: #0054aa;
    --text-light: #ffffff;
  }
  * { margin: 0; padding: 0; box-sizing: border-box; }
  html, body {
    width: 1200px;
    height: 913px;
    overflow: hidden;
    background: var(--backdrop);
  }
  .canvas {
    position: relative;
    width: 1200px;
    height: 913px;
    display: flex;
    align-items: center;
    justify-content: center;
  }
  .business-card {
    position: relative;
    width: 900px;
    height: 540px;
    background: var(--card-white);
    font-family: "Playfair Display", Georgia, serif;
    box-shadow: 0 10px 30px rgba(0,0,0,0.18);
    overflow: hidden;
  }
  .card-top {
    position: absolute;
    left: 0; top: 0;
    width: 100%;
    height: 237px;
  }
  .firm-name {
    position: absolute;
    left: 0; right: 0;
    top: 95px;
    text-align: center;
    color: var(--brand-blue);
    font-size: 28px;
    font-weight: 400;
    line-height: 34px;
  }
  .rule-thin {
    position: absolute;
    left: 0; top: 237px;
    width: 100%;
    height: 5px;
    background: var(--brand-blue);
  }
  .card-bottom {
    position: absolute;
    left: 0; top: 246px;
    width: 100%;
    height: 294px;
    background: var(--brand-blue);
    color: var(--text-light);
    text-align: center;
  }
  .person-name {
    position: absolute;
    left: 0; right: 0;
    top: 25px;
    font-size: 24px;
    line-height: 28px;
    text-transform: uppercase;
    letter-spacing: -0.3px;
  }
  .person-title {
    position: absolute;
    left: 0; right: 0;
    top: 55px;
    font-size: 21px;
    line-height: 24px;
  }
  .contact-row {
    position: absolute;
    left: 0; right: 0;
    top: 141px;
    display: flex;
    justify-content: center;
    gap: 24px;
    font-size: 17px;
    line-height: 22px;
  }
  .contact-item {
    display: flex;
    align-items: center;
    gap: 6px;
  }
  .icon-phone { width: 18px; height: 18px; fill: var(--text-light); }
  .icon-globe {
    width: 18px; height: 18px;
    fill: none;
    stroke: var(--text-light);
    stroke-width: 1.4;
  }
  .address {
    position: absolute;
    left: 0; right: 0;
    top: 251px;
    font-size: 17px;
    line-height: 22px;
  }
</style>
</head>
<body>
<div class="canvas">
  <div class="business-card">
    <div class="card-top">
      <div class="firm-name">Moss Whitfield &amp; Danby LLP</div>
    </div>
    <div class="rule-thin"></div>
    <div class="card-bottom">
      <div class="person-name">Miles Harrow</div>
      <div class="person-title">Director</div>
      <div class="contact-row">
        <span class="contact-item">
          <svg class="icon-phone" viewBox="0 0 24 24" aria-hidden="true">
            <path d="M3 8c0-2 3-4 9-4s9 2 9 4v2h-5V8.5c-1-.5-2.5-.8-4-.8s-3 .3-4 .8V10H3V8z"/>
            <path d="M7 11h10l3 8H4l3-8zm5 2a2.5 2.5 0 100 5 2.5 2.5 0 000-5z"/>
          </svg>
          (949)731-2864
        </span>
        <span class="contact-item">
          <svg class="icon-globe" viewBox="0 0 24 24" aria-hidden="true">
            <circle cx="12" cy="12" r="9"/>
            <ellipse cx="12" cy="12" rx="4" ry="9"/>
            <line x1="3" y1="12" x2="21" y2="12"/>
            <line x1="4.5" y1="7.5" x2="19.5" y2="7.5"/>
            <line x1="4.5" y1="16.5" x2="19.5" y2="16.5"/>
          </svg>
          www.mwdaccts.example
        </span>
      </div>
      <div class="address">4827 Larkspur Vale Road, Irvine, CA 92614</div>
    </div>
  </div>
</div>
</body>
</html>
```